OLU58 biz card & Stationery

LU58 is a personalized shopping experience brought to you, that lets you find and discover fashion goods through a collection of boutiques curated by taste-makers - celebrities, stylists, designers, and fashion bloggers. Boutiques uses visual technology to help fashionistas discover and shop their look and creates the opportunity for designers to showcase their collections and latest inspirations online.

OLU58 is built on technology developed by our team of fashion experts who work with engineers to “teach” our computer systems to understand various patterns, pairings, and genre definitions. When signed into your account, OLU58 learns about your style and preferences and in turn, provides you better results and recommendations over time. Ultimately, OLU58 will provide shoppers with a much richer and interactive shopping experience and help drive traffic to retailers' websites.

We need a definitely cool business card. The card must be black! And must use our official logo which can be download from OLU58.com

The address for Letter head and evenlop, please use 4872 Crestwick Parkway, Sutie 510 Los Angeles CA90412, email will be anyone@OLU58.com, website is www.OLU58.com

thanks

We received some of the design, thanks. But most of the design are not what we want. We need a very clean version with black ground, you may also use some dark gray to add the element. please take a look at http://morvalstudio.no/work/#pelter__ostrama/, we do like this kind of design very much. hope it help.

```html
<!DOCTYPE html>
<html lang="en">
<head>
<meta charset="utf-8">
<title>OLU58 Stationery</title>
<link href="https://fonts.googleapis.com/css2?family=Montserrat:wght@300;400&display=swap" rel="stylesheet">
<style>
  :root{
    --backdrop:#595959;
    --ink-black:#1c191b;
    --band-dark:#232023;
    --band-mid:#3a3739;
    --paper:#ffffff;
    --text-light:#e8e6e7;
    --text-soft:#cfcccd;
    --text-faint:#5b585a;
    --ornament:#e3e3e3;
    --ornament-dark:#3e3a3d;
  }
  *{margin:0;padding:0;box-sizing:border-box}
  html,body{width:752px;height:1200px;overflow:hidden}
  body{background:var(--backdrop);font-family:"Montserrat",Arial,sans-serif;position:relative;color:var(--text-light)}

  .card{position:absolute;top:25px;height:175px;overflow:hidden;
    background:linear-gradient(180deg,#2a262a 0%,var(--ink-black) 100%)}
  .card-front{left:80px;width:292px}
  .card-back{left:392px;width:333px}
  .wordmark{font-weight:300;letter-spacing:2px;color:var(--text-light);white-space:nowrap}
  .card-front .wordmark{position:absolute;left:36px;top:82px;font-size:34px}
  .card-ornament{position:absolute;
    background:radial-gradient(closest-side,var(--ornament-dark) 0%,rgba(62,58,61,0) 100%)}
  .card-front .card-ornament{left:140px;top:10px;width:130px;height:155px}
  .card-back .card-ornament{left:160px;top:5px;width:165px;height:165px}
  .card-back .wordmark-faint{position:absolute;left:188px;top:62px;font-size:44px;font-weight:300;
    letter-spacing:2px;color:var(--text-faint);white-space:nowrap}
  .card-back .details{position:absolute;left:26px;top:58px;width:150px;font-size:7px;line-height:11px;color:var(--text-soft)}
  .card-back .details .name{font-size:13px;line-height:18px;color:var(--text-light)}

  .letterhead{position:absolute;left:80px;top:230px;width:645px;height:795px;background:var(--paper);overflow:hidden}
  .letter-band{height:58px;background:linear-gradient(180deg,var(--band-mid) 0%,var(--band-dark) 45%,#2f2c2e 100%);position:relative}
  .letter-band .wordmark{position:absolute;left:90px;top:12px;font-size:30px}
  .letter-band .contact{position:absolute;right:22px;top:12px;text-align:right;font-size:8px;line-height:11px;color:#d6d3d4;white-space:nowrap}
  .letter-ornament{position:absolute;left:60px;top:130px;width:520px;height:560px;
    background:radial-gradient(closest-side,var(--ornament) 0%,rgba(227,227,227,.55) 50%,rgba(255,255,255,0) 100%)}

  .envelope{position:absolute;left:25px;top:1070px;width:700px;height:105px;background:var(--paper)}
  .envelope-band{position:absolute;left:0;bottom:0;width:100%;height:70px;
    background:linear-gradient(180deg,var(--band-mid) 0%,var(--band-dark) 50%,#2b282a 100%)}
  .envelope-band .return{position:absolute;left:18px;top:14px;font-size:9px;line-height:12px;color:#d6d3d4}
  .envelope-band .return .name{font-size:12px;line-height:16px;color:var(--text-light)}
</style>
</head>
<body>
  <section class="card card-front">
    <div class="card-ornament" role="img" aria-label="Faint floral swirl ornament"></div>
    <div class="wordmark">OLU58</div>
  </section>

  <section class="card card-back">
    <div class="card-ornament" role="img" aria-label="Faint floral swirl ornament"></div>
    <div class="wordmark-faint">OLU58</div>
    <div class="details">
      <div class="name">OLU58</div>
      anyone@OLU58.com<br>
      www.OLU58.com<br>
      4872 Crestwick Parkway, Sutie 510<br>
      Los Angeles CA90412
    </div>
  </section>

  <section class="letterhead">
    <header class="letter-band">
      <div class="wordmark">OLU58</div>
      <div class="contact">
        anyone@OLU58.com<br>
        www.OLU58.com<br>
        4872 Crestwick Parkway, Sutie 510 Los Angeles
      </div>
    </header>
    <div class="letter-ornament" role="img" aria-label="Large light grey floral swirl ornament"></div>
  </section>

  <section class="envelope">
    <div class="envelope-band">
      <div class="return">
        <div class="name">OLU58</div>
        4872 Crestwick Parkway, Sutie 510<br>
        Los Angeles CA90412
      </div>
    </div>
  </section>
</body>
</html>
```